Disable Adaptations& Specialised Equipment Occupational Therapist Product Brochure

We need a product brochure put together containing the equipment and services we can provide and deal with. Aimed at the Occupational Therapists , Social Services, Local Councils and Housing associations we work with it needs to have a professional but simple layout that is easy to capture the intended.We are based in Mid- Suffolk , East Anglia and we provide basic and specialised equipment . Ideally three fold brochure design front and back, our company colours are green and grey . Please see the power point brochure we have put together ourselves and re design .

Please use the Template below for the brochure:

PSD template - http://www.quillmark-prints.example/propath/download-template.aspx?Log=1&path=propath&pfid=150&pf_id=150&type=2
AI template - http://www.quillmark-prints.example/propath/download-template.aspx?Log=1&path=propath&pfid=150&pf_id=150&type=3

Full Bleed Size
282 x 219 mm
3331 x 2588 pixels
Document Trim Size
279 x 216 mm
3295 x 2551 pixels

Industry/Entity Type

It Company

Requirements
Must have
• Address and Telephone number 01632 960417
To show map of areas covered in East Anglia opposed to business position

```html
<!DOCTYPE html>
<html lang="en">
<head>
<meta charset="utf-8">
<title>Orwell Mobility Systems – Product Brochure</title>
<link href="https://fonts.googleapis.com/css2?family=Open+Sans:wght@400;600;700&family=PT+Sans+Narrow:wght@400;700&display=swap" rel="stylesheet">
<style>
  :root{
    --green:#8cc63f;
    --green-dark:#6fae2b;
    --grey-bg:#d9d9d9;
    --grey-text:#4a4a4a;
    --grey-logo:#8c8c8c;
    --map-tone:#b9d98f;
    --white:#ffffff;
    --page:#e6e6e6;
  }
  *{margin:0;padding:0;box-sizing:border-box}
  html,body{width:1200px;height:1000px;overflow:hidden;background:var(--page)}
  body{font-family:"Open Sans",Arial,sans-serif;color:var(--grey-text)}
  .brochure{position:absolute;left:18px;top:50px;width:1164px;height:900px;display:flex;box-shadow:0 4px 18px rgba(0,0,0,.18)}
  .panel{position:relative;width:388px;height:900px;overflow:hidden}
  .panel--white{background:var(--white)}
  .panel--green{background:var(--green)}
  .title-band{position:absolute;left:18px;top:50px;width:1164px;height:58px;background:var(--green);z-index:2;display:flex;align-items:center;justify-content:center}
  .title-band h1{color:var(--white);font-size:24px;font-weight:600;letter-spacing:.2px}
  .photo{position:absolute;border-radius:6px}
  .item{position:absolute;width:170px}
  .item h2{font-size:15px;font-weight:600;color:var(--green);line-height:1.2}
  .item p{font-family:"PT Sans Narrow","Arial Narrow",sans-serif;font-weight:400;font-size:14px;line-height:1.25;color:var(--grey-text)}
  .panel--green .item h2,.panel--green .item p{color:var(--white)}
  .arrow{display:block;width:56px;height:30px;margin-bottom:2px}
  .contact-area{position:absolute;left:0;bottom:0;width:388px;height:180px;background:linear-gradient(#f2f2f2,var(--grey-bg));display:flex;align-items:center;gap:14px;padding:0 20px}
  .coverage-map{flex:0 0 100px;height:120px;border-radius:6px;background:linear-gradient(160deg,var(--map-tone),var(--green))}
  .contact-details{display:flex;flex-direction:column;gap:6px}
  .brand{display:flex;align-items:center;gap:8px}
  .brand .dot{width:22px;height:22px;border-radius:50%;background:var(--green);flex:0 0 22px}
  .brand .company{font-size:17px;font-weight:600;color:var(--grey-logo);line-height:1.2}
  .contact-line{display:flex;align-items:flex-start;gap:6px;font-family:"PT Sans Narrow","Arial Narrow",sans-serif;font-size:14px;line-height:1.25;color:var(--grey-text)}
  .contact-line svg{flex:0 0 14px;width:14px;height:14px;margin-top:2px;color:var(--green)}
  .coverage-note{font-family:"PT Sans Narrow","Arial Narrow",sans-serif;font-size:13px;color:var(--grey-logo)}
</style>
</head>
<body>
<svg width="0" height="0" style="position:absolute">
  <defs>
    <symbol id="curve-arrow" viewBox="0 0 56 30">
      <path d="M4 26 Q28 26 44 10" fill="none" stroke="currentColor" stroke-width="4" stroke-linecap="round"/>
      <path d="M36 6 L50 4 L47 18 Z" fill="currentColor"/>
    </symbol>
    <symbol id="icon-phone" viewBox="0 0 24 24">
      <path d="M6.6 10.8a15 15 0 0 0 6.6 6.6l2.2-2.2a1 1 0 0 1 1-.25 11.4 11.4 0 0 0 3.6.57 1 1 0 0 1 1 1V20a1 1 0 0 1-1 1A17 17 0 0 1 3 4a1 1 0 0 1 1-1h3.5a1 1 0 0 1 1 1c0 1.25.2 2.45.57 3.57a1 1 0 0 1-.25 1z" fill="currentColor"/>
    </symbol>
    <symbol id="icon-pin" viewBox="0 0 24 24">
      <path d="M12 2a7 7 0 0 0-7 7c0 5.2 7 13 7 13s7-7.8 7-13a7 7 0 0 0-7-7zm0 9.5A2.5 2.5 0 1 1 12 6.5a2.5 2.5 0 0 1 0 5z" fill="currentColor"/>
    </symbol>
  </defs>
</svg>

<div class="title-band"><h1>Orwell Mobility Systems – For All Your Specialist Equipment Needs</h1></div>

<main class="brochure">
  <section class="panel panel--white">
    <div class="photo" role="img" aria-label="Pink specialist recliner chair with cushions" style="left:20px;top:80px;width:140px;height:170px;background:linear-gradient(160deg,#b24a6b,#f08fb4)"></div>
    <div class="item" style="left:175px;top:82px;width:190px">
      <svg class="arrow" style="color:var(--green)"><use href="#curve-arrow"/></svg>
      <h2>Specialist seating</h2>
      <p>From standard and made to measure rise and recliners to specialist seating with in built pressure care and support</p>
    </div>

    <div class="photo" role="img" aria-label="Wooden four section profiling bed" style="left:50px;top:285px;width:310px;height:110px;background:linear-gradient(160deg,#c98a4c,#b8b8b8)"></div>
    <div class="item" style="left:20px;top:400px;width:330px">
      <svg class="arrow" style="color:var(--green)"><use href="#curve-arrow"/></svg>
      <h2>Profiling beds</h2>
      <p>Top quality four section rise and fall profiling beds</p>
    </div>

    <div class="photo" role="img" aria-label="Teal and navy pressure care armchairs" style="left:50px;top:505px;width:290px;height:200px;background:linear-gradient(90deg,#2f7f7a 0%,#3d8e86 45%,#1d2648 55%,#2a3260 100%)"></div>
    <div class="item" style="left:20px;top:730px;width:330px">
      <svg class="arrow" style="color:var(--green)"><use href="#curve-arrow"/></svg>
      <h2>Pressure Care</h2>
      <p>From the standard Cushara cushion range through to low, medium and high risk professional mattresses</p>
    </div>
  </section>

  <section class="panel panel--green">
    <div class="photo" role="img" aria-label="Free standing gantry hoist frame" style="left:40px;top:90px;width:310px;height:180px;background:linear-gradient(#f4f4f4,#dcdcdc)"></div>
    <div class="item" style="left:140px;top:278px;width:220px">
      <svg class="arrow" style="color:var(--white)"><use href="#curve-arrow"/></svg>
      <h2>Gantry systems</h2>
      <p>Professional easy to install, mobile gantry systems</p>
    </div>

    <div class="photo" role="img" aria-label="Wheeled shower commode chair" style="left:20px;top:395px;width:165px;height:215px;background:linear-gradient(#e0e0e0,#9a9a9a)"></div>
    <div class="photo" role="img" aria-label="Tilt in space wheelchair" style="left:200px;top:395px;width:170px;height:145px;background:linear-gradient(#d8d8d8,#7a7a7a)"></div>
    <div class="item" style="left:200px;top:545px;width:180px">
      <svg class="arrow" style="color:var(--white)"><use href="#curve-arrow"/></svg>
      <h2>Wheelchairs</h2>
      <p>From basic attendant wheelchairs through to the more complex fully adaptable chairs</p>
    </div>

    <div class="photo" role="img" aria-label="Tilt in space shower chair" style="left:165px;top:680px;width:205px;height:180px;background:linear-gradient(#f2f2f2,#c8c8c8)"></div>
    <div class="item" style="left:20px;top:700px;width:135px">
      <svg class="arrow" style="color:var(--white)"><use href="#curve-arrow"/></svg>
      <h2>Shower chairs</h2>
      <p>A full range of shower chairs from basic entry level to manual and electric Tilt In Space</p>
    </div>
  </section>

  <section class="panel panel--white">
    <div class="item" style="left:20px;top:68px;width:200px">
      <h2>Bathroom aids</h2>
      <p>Everything from the very basic bath boards and toilet seat raisers</p>
    </div>
    <div class="photo" role="img" aria-label="Raised toilet seat with arms" style="left:25px;top:150px;width:130px;height:120px;background:linear-gradient(#f6f6f6,#d4d4d4)"></div>
    <div class="photo" role="img" aria-label="Ceiling track hoist unit" style="left:205px;top:120px;width:150px;height:150px;background:linear-gradient(#bdbdbd,#e8e8e8)"></div>
    <div class="item" style="left:20px;top:272px;width:160px">
      <svg class="arrow" style="color:var(--green)"><use href="#curve-arrow"/></svg>
      <h2>Commodes</h2>
      <p>A full range of static and wheeled commodes</p>
    </div>
    <div class="item" style="left:200px;top:272px;width:180px">
      <svg class="arrow" style="color:var(--green)"><use href="#curve-arrow"/></svg>
      <h2>Ceiling hoists</h2>
      <p>The very latest technology fully installed and tested</p>
    </div>

    <div class="photo" role="img" aria-label="Mobile patient hoist" style="left:25px;top:385px;width:145px;height:195px;background:linear-gradient(#eeeeee,#9c9c9c)"></div>
    <div class="photo" role="img" aria-label="Electric stand aid" style="left:210px;top:385px;width:140px;height:150px;background:linear-gradient(#f0f0f0,#b4b4b4)"></div>
    <div class="item" style="left:200px;top:540px;width:180px">
      <svg class="arrow" style="color:var(--green)"><use href="#curve-arrow"/></svg>
      <h2>Electric stand aids</h2>
      <p>New modern electric stand aids</p>
    </div>
    <div class="item" style="left:20px;top:585px;width:175px">
      <svg class="arrow" style="color:var(--green)"><use href="#curve-arrow"/></svg>
      <h2>Mobile hoists</h2>
      <p>From the standard hydraulic hoists through to top of the range electric versions</p>
    </div>

    <div class="contact-area">
      <div class="coverage-map" role="img" aria-label="Map of areas covered across East Anglia"></div>
      <div class="contact-details">
        <div class="brand">
          <span class="dot"></span>
          <span class="company">Orwell Mobility Systems Ltd</span>
        </div>
        <div class="contact-line">
          <svg><use href="#icon-phone"/></svg>
          <span>01632 960417</span>
        </div>
        <div class="contact-line">
          <svg><use href="#icon-pin"/></svg>
          <span>Unit 4, Kestrel Park, Needham Lane, Suffolk IP0 4QX</span>
        </div>
        <div class="coverage-note">Covering Suffolk, Norfolk and Essex</div>
      </div>
    </div>
  </section>
</main>
</body>
</html>
```